larvoo.net

We are a IT Service for the valley. I want a clean website, with new Design, like animated pictures. We focus on IT. Give me your best design. What I'm looking for is eye catching. Works with Smart Phones, and iPad, Tab. Need a section for Submit a support tickets and Remote support. I'm looking for new ideals. I'm open mind, let me see what you guys can do.

Target Market(s)

My clients to see what service and products we have.

Industry/Entity Type

It Service

Requirements
Must have
• Able to submit a trouble tickets and works with Smart Phones, iPad, Tab.

```html
<!DOCTYPE html>
<html lang="en">
<head>
<meta charset="utf-8">
<title>Larvoo Technology</title>
<link rel="stylesheet" href="https://fonts.googleapis.com/css2?family=Montserrat:wght@300&family=Open+Sans:wght@400;600;700&family=PT+Serif&display=swap">
<style>
:root{
  --navy:#1f2a56;
  --ink:#222;
  --text:#444;
  --muted:#555;
  --red:#d71f26;
  --line:#e2e2e2;
  --link:#6a8fdc;
  --white:#fff;
}
*{box-sizing:border-box;margin:0;padding:0}
h1,h2,h3{font-weight:400}
html,body{width:939px;height:1200px;overflow:hidden;background:var(--white)}
body{position:relative;font-family:"Open Sans",Arial,sans-serif;color:var(--text)}
a{text-decoration:none;color:inherit}
.abs{position:absolute}

.top-bar{left:0;top:0;width:939px;height:3px;background:#111}
.top-notch{left:452px;top:0}

.brand{left:118px;top:36px;color:var(--navy);font-weight:600;line-height:1}
.brand-name{font-size:34px;letter-spacing:1px}
.brand-sub{font-size:11px;letter-spacing:8.6px;margin-top:4px;padding-left:2px}

.nav{top:46px;display:flex;flex-direction:column;align-items:center;font-family:"PT Serif",Georgia,serif;font-size:11px;color:var(--ink);text-transform:uppercase}
.nav svg{margin-bottom:6px}
.nav.is-active{color:var(--red)}
.nav-home{left:514px}
.nav-services{left:588px}
.nav-products{left:679px}
.nav-contact{left:777px}

.rule{left:8px;width:931px;height:1px;background:var(--line)}
.rule-top{top:118px}
.rule-bottom{top:446px}
.shade{left:180px;width:580px;height:30px;border-radius:50%;background:radial-gradient(ellipse at center,rgba(0,0,0,.10),rgba(0,0,0,0) 70%)}
.shade-top{top:88px}
.shade-bottom{top:446px}

.hero-title{left:140px;top:151px;font-family:Arial,Helvetica,sans-serif;font-weight:700;font-size:29px;line-height:34px;color:var(--red)}
.hero-lead{left:142px;top:240px;font-family:Arial,Helvetica,sans-serif;font-size:17.6px;color:#111}
.hero-list{left:172px;top:288px;list-style:none;font-family:Arial,Helvetica,sans-serif;font-size:11px;color:var(--muted)}
.hero-list li{display:flex;align-items:center;height:25px}
.hero-list svg{margin-right:6px}
.hero-visual{left:418px;top:140px;width:404px;height:278px;border-radius:6px;background:linear-gradient(135deg,#3a2a1a 0%,#8a4a14 30%,#e9eef2 52%,#1d8ab8 70%,#dfe3e6 100%)}

.slide-arrow{top:228px;width:28px;height:57px;background:linear-gradient(#eee,#d6d6d6);border-radius:3px;display:flex;align-items:center;justify-content:center}
.slide-prev{left:82px}
.slide-next{left:829px}

.btn{display:flex;align-items:center;justify-content:center;gap:8px;font-family:"PT Serif",Georgia,serif;font-size:14px;border-radius:5px}
.btn-light{left:128px;top:389px;width:131px;height:35px;color:var(--navy);background:linear-gradient(#fff,#e4e4e4);border:1px solid #d4d4d4;box-shadow:0 4px 6px rgba(0,0,0,.12)}
.btn-dark{left:673px;top:565px;width:116px;height:36px;color:var(--white);background:linear-gradient(#4a5787,#25305e);border:1px solid #1b244b;box-shadow:0 5px 8px rgba(0,0,0,.18)}

.welcome{left:110px;top:487px;width:718px;height:156px;border:1px solid #cfcfcf;border-radius:5px}
.welcome-title{left:141px;top:500px;font-family:"PT Serif",Georgia,serif;font-size:25px;line-height:25px;color:#555}
.welcome-title span{color:var(--navy)}
.welcome-text{left:142px;top:573px;width:450px;font-size:13.4px;line-height:19.5px;color:var(--text)}

.services-title{left:110px;top:664px;font-family:"PT Serif",Georgia,serif;font-size:21px;color:#111}
.services-tagline{left:110px;top:700px;font-family:Montserrat,Arial,sans-serif;font-weight:300;font-size:19.3px;line-height:25px;color:var(--red);text-transform:uppercase;white-space:nowrap}

.feature{width:230px}
.feature-head{display:flex;align-items:center;gap:13px;height:26px}
.feature-icon{width:24px;height:24px;border-radius:4px}
.feature-name{font-family:Arial,Helvetica,sans-serif;font-weight:700;font-size:12px;color:var(--navy);text-transform:uppercase}
.feature-text{font-size:12px;line-height:16.5px;color:var(--text);margin-top:5px}

.footer{left:0;top:997px;width:939px;height:203px;background:var(--navy)}
.footer-head{top:1022px;font-family:"PT Serif",Georgia,serif;font-size:16px;color:var(--white);text-transform:uppercase}
.footer-list{top:1050px;list-style:none;font-size:10px;line-height:20.7px;color:var(--link)}
.footer-rule{left:110px;top:1152px;width:718px;height:1px;background:#34407a}
.copyright{left:110px;top:1171px;font-size:10px;color:var(--link)}
.social{top:1167px;width:22px;height:22px;background:#3b63b5}
</style>
</head>
<body>

<div class="abs top-bar"></div>
<svg class="abs top-notch" width="34" height="18" viewBox="0 0 34 18"><path d="M0 0h34L17 16z" fill="#111"/><path d="M8 2l9 8 9-8" fill="none" stroke="#fff" stroke-width="2"/></svg>

<header>
  <div class="abs brand">
    <div class="brand-name">LARVOO</div>
    <div class="brand-sub">TECHNOLOGY</div>
  </div>

  <a class="abs nav nav-home is-active">
    <svg width="14" height="13" viewBox="0 0 14 13"><path d="M7 0L0 6h2v7h4V9h2v4h4V6h2z" fill="#d71f26"/></svg>Home
  </a>
  <a class="abs nav nav-services">
    <svg width="15" height="14" viewBox="0 0 15 14"><path d="M2 1l11 12M13 1L2 13" stroke="#111" stroke-width="2.4"/></svg>Services &#9662;
  </a>
  <a class="abs nav nav-products">
    <svg width="20" height="13" viewBox="0 0 20 13"><rect x="1" y="3" width="18" height="9" rx="1" fill="none" stroke="#111" stroke-width="1.4"/><path d="M4 6h12M4 9h12M10 0v3" stroke="#111"/></svg>Products
  </a>
  <a class="abs nav nav-contact">
    <svg width="16" height="13" viewBox="0 0 16 13"><rect x="1" y="1" width="14" height="11" fill="none" stroke="#111" stroke-width="1.4"/><path d="M1 1l7 6 7-6M1 12l5-5M15 12l-5-5" fill="none" stroke="#111"/></svg>Contact
  </a>
</header>

<div class="abs shade shade-top"></div>
<div class="abs rule rule-top"></div>

<section class="hero">
  <div class="abs slide-arrow slide-prev"><svg width="10" height="16" viewBox="0 0 10 16"><path d="M8 2L2 8l6 6" fill="none" stroke="#fff" stroke-width="3"/></svg></div>
  <h1 class="abs hero-title">Website Design &amp;<br>Development</h1>
  <p class="abs hero-lead">We will build your dream website</p>
  <ul class="abs hero-list">
    <li><svg width="12" height="10" viewBox="0 0 12 10"><path d="M1 5l3.5 3.5L11 1" fill="none" stroke="#4caf50" stroke-width="2.2"/></svg>Professional Website Design &amp; reDesign</li>
    <li><svg width="12" height="10" viewBox="0 0 12 10"><path d="M1 5l3.5 3.5L11 1" fill="none" stroke="#4caf50" stroke-width="2.2"/></svg>Custom User Friendly Design</li>
    <li><svg width="12" height="10" viewBox="0 0 12 10"><path d="M1 5l3.5 3.5L11 1" fill="none" stroke="#4caf50" stroke-width="2.2"/></svg>Using Cutting Edge Web Technologies</li>
  </ul>
  <a class="abs btn btn-light">Explore More <svg width="8" height="11" viewBox="0 0 8 11"><path d="M1.5 1.5l4 4-4 4" fill="none" stroke="#1f2a56" stroke-width="2.4"/></svg></a>
  <div class="abs hero-visual" role="img" aria-label="Two desktop monitors showing sample website designs"></div>
  <div class="abs slide-arrow slide-next"><svg width="10" height="16" viewBox="0 0 10 16"><path d="M2 2l6 6-6 6" fill="none" stroke="#fff" stroke-width="3"/></svg></div>
</section>

<div class="abs rule rule-bottom"></div>
<div class="abs shade shade-bottom"></div>

<section>
  <div class="abs welcome"></div>
  <h2 class="abs welcome-title">Welcome to<br><span>Larvoo Technology</span></h2>
  <p class="abs welcome-text">Founded in 2004, Larvoo Technology focus on quality of their products, along with their customer service to ensure both lengthy uptimes while also minimizing downtime.</p>
  <a class="abs btn btn-dark">Get Started <svg width="8" height="11" viewBox="0 0 8 11"><path d="M1.5 1.5l4 4-4 4" fill="none" stroke="#fff" stroke-width="2.4"/></svg></a>
</section>

<section>
  <h2 class="abs services-title">Services</h2>
  <p class="abs services-tagline">What is your brand's rep? Do the right people know it?<br>It all starts with making a good impression. That's what we do.</p>

  <div class="abs feature" style="left:112px;top:782px">
    <div class="feature-head"><div class="feature-icon" role="img" aria-label="Accessibility icon" style="background:#8fb8e6"></div><span class="feature-name">Accessibility</span></div>
    <p class="feature-text">On-Call and ready to serve your needs.<br>Service is only a phone call away.</p>
  </div>
  <div class="abs feature" style="left:392px;top:782px">
    <div class="feature-head"><div class="feature-icon" role="img" aria-label="Thumbs up icon" style="background:#e9b88a"></div><span class="feature-name">Turn Around Time</span></div>
    <p class="feature-text">We Fix your network problem<br>in a timely manner.</p>
  </div>
  <div class="abs feature" style="left:636px;top:782px">
    <div class="feature-head"><div class="feature-icon" role="img" aria-label="Computer monitor icon" style="background:#9fc4e4"></div><span class="feature-name">Quality Products</span></div>
    <p class="feature-text">Provide hardware or software that<br>will suit your specific needs.</p>
  </div>
  <div class="abs feature" style="left:112px;top:885px">
    <div class="feature-head"><div class="feature-icon" role="img" aria-label="Globe icon" style="background:#3d6fb0;border-radius:50%"></div><span class="feature-name">Longevity</span></div>
    <p class="feature-text">Building a long-term, trusting,<br>relationship is our goal.</p>
  </div>
  <div class="abs feature" style="left:392px;top:885px">
    <div class="feature-head"><div class="feature-icon" role="img" aria-label="Consultant icon" style="background:#2f4a80"></div><span class="feature-name">Consultation</span></div>
    <p class="feature-text">We consult you on proper upgrades<br>or purchases for your company.</p>
  </div>
  <div class="abs feature" style="left:636px;top:885px">
    <div class="feature-head"><div class="feature-icon" role="img" aria-label="Smile icon" style="background:#f3c623;border-radius:50%"></div><span class="feature-name">Troubleshooting</span></div>
    <p class="feature-text">&nbsp;We will solve your network<br>problems with a friendly smile.</p>
  </div>
</section>

<footer>
  <div class="abs footer"></div>
  <h3 class="abs footer-head" style="left:112px">Quick Links</h3>
  <ul class="abs footer-list" style="left:112px"><li>Home</li><li>Services</li><li>Products</li><li>Contact Us</li></ul>
  <h3 class="abs footer-head" style="left:262px">Support</h3>
  <ul class="abs footer-list support-list" style="left:262px"><li><a href="#ticket">Submit a Ticket</a></li><li><a href="#remote">Remote Support</a></li></ul>
  <h3 class="abs footer-head" style="left:407px">Services List</h3>
  <ul class="abs footer-list" style="left:407px"><li>Clearline VOIP Phones</li><li>Network Server</li><li>Desktop Workstation</li><li>Web Design</li></ul>
  <h3 class="abs footer-head" style="left:692px">Contace Info</h3>
  <ul class="abs footer-list" style="left:692px;line-height:16px;top:1052px"><li>482 N. Orchard Street,</li><li>Valley City, CA 93201</li><li>Office phone:&nbsp;&nbsp; (555) 014-2273</li></ul>
  <div class="abs footer-rule"></div>
  <p class="abs copyright">Copyright &copy; 2012 Larvoo Technology. All Rights Reserved.</p>
  <div class="abs social" style="left:748px" role="img" aria-label="Social link"></div>
  <div class="abs social" style="left:778px;background:#1da1e8" role="img" aria-label="Social link"></div>
  <div class="abs social" style="left:808px;background:#0a7ab8" role="img" aria-label="Social link"></div>
</footer>

</body>
</html>
```